PREVENTING FALLS IN YOUR HOME / MAKING YOUR HOME SAFER

We sell, and install grab bars for only $99 each in the home. Statistics to present: 2.8 million people are treated in emergency rooms annually for falls. 800,000 are hospitalized because of fall injury. 95% of hip fractures are caused by falling. I would like a 1 page marketing piece containing a cartoon like male slipping backwards holding on to shower curtain which is bending curtain rod that cannot support him. Then as a don't and do,same man wisely entering tub using grab bar. Slipping on stairs, trying to grab onto whatever won't hold him would be another scenario.
Included in piece would be above fall statistics separated into bursts, reminder that grab bars can be installed in any room including the garage and a star burst of Only $99, includes bar and installation and

Target Market(s)

over 50 year old market butpredominantly elderly population

Industry/Entity Type

Home Health Care

Font styles to use
Sans Serif

Colors
ec1f27

Requirements
Must have
• instant recognition that a grab bar can prevent serious falls and hip fracture. The cartoon characterization must make instant understanding without reading text
Nice to have
• large print
• concise message
• not a lot of reading to understand
• cartoons in circle with line through don' t circle Ie. no swimming
Should not have
• small print
• congested page

```html
<!DOCTYPE html>
<html lang="en">
<head>
<meta charset="utf-8">
<title>Safety Grab Bars – Falls &amp; slip accidents are no joke!</title>
<link rel="stylesheet" href="https://fonts.googleapis.com/css2?family=Fira+Sans+Extra+Condensed:wght@600;700;800;900&family=Fira+Sans:wght@700;800;900&display=swap">
<style>
  :root {
    --sky: #cde6f7;
    --ink: #1a1a1a;
    --red: #ec1f27;
    --deep-red: #cf161b;
    --yellow: #ffe500;
    --band-blue: #0a9fe3;
    --white: #ffffff;
  }
  * { margin: 0; padding: 0; box-sizing: border-box; }
  html, body { width: 927px; height: 1200px; overflow: hidden; background: var(--sky); }
  .flyer {
    position: relative;
    width: 927px;
    height: 1200px;
    overflow: hidden;
    background: var(--sky);
    font-family: "Fira Sans Extra Condensed", "Arial Narrow", sans-serif;
  }
  .abs { position: absolute; }

  .headline {
    left: 0; width: 927px; text-align: center;
    font-weight: 900; color: var(--ink);
    letter-spacing: -2px; line-height: 1;
    -webkit-text-stroke: 10px var(--white);
    paint-order: stroke fill;
    white-space: nowrap;
  }
  .headline--top { top: 34px; font-size: 106px; }
  .headline--bottom { top: 164px; font-size: 106px; }
  .headline .accent { color: var(--deep-red); }

  .cartoon-area {
    left: 216px; top: 264px; width: 688px; height: 384px;
    border-radius: 12px;
    background: linear-gradient(90deg, #f3c2d8 0%, #e8a7c6 45%, #f5dcc6 100%);
  }

  .burst { left: 0; top: 0; width: 927px; height: 1200px; }
  .burst-text { text-align: center; line-height: 1; }
  .stat-hip { left: 10px; top: 226px; width: 190px; }
  .stat-hip .big { font-size: 62px; font-weight: 900; color: var(--yellow); }
  .stat-hip .small { font-size: 26px; font-weight: 700; color: var(--white); line-height: 0.98; }
  .stat-hosp { left: 36px; top: 416px; width: 210px; color: var(--deep-red); }
  .stat-hosp .big { font-size: 40px; font-weight: 800; }
  .stat-hosp .small { font-size: 21px; font-weight: 700; }
  .stat-hosp .huge { font-size: 52px; font-weight: 800; line-height: 0.9; }

  .red-ground { left: 0; top: 0; width: 927px; height: 1200px; }

  .product-band {
    left: 86px; top: 648px; width: 718px; height: 82px;
    background: var(--band-blue);
    color: var(--white);
    font-family: "Fira Sans", sans-serif;
    font-weight: 800; font-size: 62px;
    text-align: center; line-height: 82px; letter-spacing: 0.5px;
  }

  .where-line {
    left: 0; width: 862px; top: 742px; text-align: center;
    color: var(--white); font-weight: 800; font-size: 35px; line-height: 41px;
    letter-spacing: -1px;
    -webkit-text-stroke: 5px var(--ink); paint-order: stroke fill;
  }

  .install-from {
    left: 60px; width: 310px; top: 872px; text-align: right;
    color: var(--white); font-weight: 800; font-size: 39px; line-height: 43px;
  }
  .benefits {
    left: 60px; width: 310px; top: 960px; text-align: right;
    color: var(--white); font-weight: 700; font-size: 21px; line-height: 33px;
    list-style: none;
  }
  .tick { display: inline-block; width: 20px; height: 16px; margin: 0 4px 0 10px; vertical-align: -1px; }

  .price {
    left: 394px; top: 838px;
    font-family: "Fira Sans", sans-serif; font-weight: 900;
    font-size: 245px; line-height: 1; letter-spacing: -10px;
    color: var(--white);
    -webkit-text-stroke: 14px var(--ink); paint-order: stroke fill;
  }
  .price-mark {
    left: 750px; top: 826px;
    font-family: "Fira Sans", sans-serif; font-weight: 900;
    font-size: 104px; line-height: 1; color: var(--white);
    -webkit-text-stroke: 10px var(--ink); paint-order: stroke fill;
  }

  .order {
    left: 0; width: 927px; top: 1078px; text-align: center;
    color: var(--white); font-weight: 700; font-size: 54px; line-height: 1;
    white-space: nowrap;
  }
  .phone-icon { display: inline-block; width: 42px; height: 42px; vertical-align: -4px; margin: 0 6px 0 4px; }
  .visit {
    left: 0; width: 927px; top: 1136px; text-align: center;
    color: var(--white); font-weight: 700; font-size: 35px; line-height: 1;
  }
</style>
</head>
<body>
<main class="flyer">
  <div class="abs cartoon-area" role="img" aria-label="Cartoon: an elderly man slips while clutching a pink shower curtain, crossed out in red; beside him the same man safely holds a wall grab bar, marked with a red tick"></div>

  <h1>
    <span class="abs headline headline--top">Falls &amp; slip accidents</span>
    <span class="abs headline headline--bottom">are <span class="accent">no joke!</span></span>
  </h1>

  <svg class="abs burst" viewBox="0 0 927 1200" aria-hidden="true">
    <polygon fill="var(--deep-red)" points="
      104,180 115,193 130,183 137,198 154,192 157,209 174,207 173,224 190,226 185,242 201,249 192,263 206,273 194,285 206,298 192,306 202,320 186,326 192,342 175,345 177,362 160,361 158,378 142,374 136,390 121,383 112,396 100,386 88,396 80,383 64,390 58,374 42,378 40,361 23,362 25,345 8,342 14,326 -2,320 8,306 -6,298 6,285 -6,273 8,263 -1,249 15,242 10,226 27,224 26,207 43,209 46,192 63,198 70,183 85,193 96,180"/>
    <polygon fill="var(--yellow)" points="
      140,380 151,393 166,385 174,400 190,395 194,412 211,411 211,428 228,431 224,447 240,454 232,469 246,480 235,492 246,504 232,515 240,530 224,537 228,553 211,556 211,573 194,572 190,589 174,584 166,599 151,591 140,604 129,591 114,599 106,584 90,589 86,572 69,573 69,556 52,553 56,537 40,530 48,515 34,504 45,492 34,480 48,469 40,454 56,447 52,431 69,428 69,411 86,412 90,395 106,400 114,385 129,393"/>
  </svg>

  <div class="abs burst-text stat-hip">
    <div class="big">95%</div>
    <div class="small">of hip fractures<br>are caused by<br>falling!</div>
  </div>
  <div class="abs burst-text stat-hosp">
    <div class="big">800,000</div>
    <div class="small">hospitalized due to</div>
    <div class="huge">FALL<br>INJURY</div>
  </div>

  <svg class="abs red-ground" viewBox="0 0 927 1200" aria-hidden="true">
    <path fill="var(--deep-red)" d="M0,758 C260,720 560,690 927,690 L927,1200 L0,1200 Z"/>
  </svg>

  <h2 class="abs product-band">SAFETY GRAB BARS</h2>

  <p class="abs where-line">FOR YOUR BATHROOM, BY YOUR STAIRS, OR ANYWHERE<br>IN YOUR HOME WHERE SLIPS CAN HAPPEN!</p>

  <p class="abs install-from">PROFESSIONALLY<br>INSTALLED FROM</p>
  <ul class="abs benefits">
    <li><svg class="tick" viewBox="0 0 20 16"><path d="M2,8 L8,14 L18,2" fill="none" stroke="var(--yellow)" stroke-width="4" stroke-linecap="round" stroke-linejoin="round"/></svg>STABILITY<svg class="tick" viewBox="0 0 20 16"><path d="M2,8 L8,14 L18,2" fill="none" stroke="var(--yellow)" stroke-width="4" stroke-linecap="round" stroke-linejoin="round"/></svg>EXTRA SUPPORT</li>
    <li><svg class="tick" viewBox="0 0 20 16"><path d="M2,8 L8,14 L18,2" fill="none" stroke="var(--yellow)" stroke-width="4" stroke-linecap="round" stroke-linejoin="round"/></svg>AFFORDABLE PEACE OF MIND</li>
  </ul>

  <p class="abs price">$99</p>
  <span class="abs price-mark">*</span>

  <p class="abs order">Order yours!<svg class="phone-icon" viewBox="0 0 24 24"><path fill="var(--yellow)" d="M6.6 10.8c1.4 2.8 3.8 5.1 6.6 6.6l2.2-2.2c.3-.3.7-.4 1-.2 1.1.4 2.3.6 3.600.6.6 0 1 .4 1 1V20c0 .6-.4 1-1 1C10.6 21 3 13.4 3 4c0-.6.4-1 1-1h3.5c.6 0 1 .4 1 1 0 1.3.2 2.5.6 3.6.1.3 0 .7-.2 1l-2.3 2.2z"/></svg>800-555-0142</p>
  <p class="abs visit">or visit www.steadyhomesafety.com</p>
</main>
</body>
</html>
```